Sticker Design for Company Equipment - Velnorix

We are looking for a professional and clean graphic design for a set of stickers to apply on our company equipment (cleaning, gardening, pest control). The stickers must include our logo (the square with the three colored segments and the checkmark), our phone number, email address, and website, you can decide to use all three or just our website based on your graphic needs. It is important that it has an attractive sharp and clear look. The design should be consistent with our brand identity and give a polished, trustworthy look to our tools and machinery. We need a modular design that works in different formats (rectangular, square, round), depending on the type of equipment.

Need extra days to review

```html
<!DOCTYPE html>
<html lang="en">
<head>
<meta charset="utf-8">
<title>Velnorix – Equipment Stickers</title>
<link rel="stylesheet" href="https://fonts.googleapis.com/css2?family=Montserrat:wght@400;500;600;700&display=swap">
<style>
:root{
  --navy:#29285f;
  --green:#7ab53f;
  --orange:#e0672b;
  --white:#ffffff;
  --paper:#ffffff;
  --shadow:0 3px 7px rgba(0,0,0,.32);
}
*{box-sizing:border-box;margin:0;padding:0}
html,body{width:738px;height:1200px;overflow:hidden;background:var(--paper)}
body{position:relative;font-family:"Montserrat",Arial,sans-serif;color:var(--white)}
.sticker{position:absolute;background:var(--white);box-shadow:var(--shadow)}
.abs{position:absolute}
.wordmark{position:absolute;font-weight:700;line-height:1;letter-spacing:1px;white-space:nowrap}
.wordmark--white{color:var(--white)}
.wordmark--navy{color:var(--navy)}
.brand-square{position:absolute}
.line{position:absolute;display:flex;align-items:center;white-space:nowrap;line-height:1}
.icon{flex:none;fill:currentColor}
.hidden-defs{position:absolute;width:0;height:0;overflow:hidden}

/* Sticker 1 – rounded band */
.s1{left:125px;top:116px;width:500px;height:175px;border-radius:26px}
.s1__inner{position:absolute;left:10px;top:11px;width:480px;height:154px;border-radius:20px;overflow:hidden;background:var(--navy)}
.s1__top{position:absolute;left:0;top:0;width:100%;height:41px;background:var(--green)}
.s1__bottom{position:absolute;left:0;bottom:0;width:100%;height:42px;background:var(--orange)}
.s1__swoosh{position:absolute;left:0;top:0}

/* Sticker 2 – wide */
.s2{left:97px;top:377px;width:549px;height:126px}
.tagline{position:absolute;left:132px;top:61px;font-size:15.5px;font-weight:600;letter-spacing:2.3px;white-space:nowrap;line-height:1}
.tagline .c-navy{color:var(--navy)}
.tagline .c-green{color:var(--green)}
.tagline .c-orange{color:var(--orange)}
.contact-bar{position:absolute;top:88px;height:29px;font-size:10.5px;font-weight:500}
.badge{position:absolute;top:-3px;left:-10px;width:23px;height:23px;border-radius:50%;background:var(--white);border:2px solid;display:flex;align-items:center;justify-content:center}

/* Sticker 3 – compact */
.s3{left:168px;top:598px;width:423px;height:202px}

/* Sticker 4 – full */
.s4{left:123px;top:901px;width:504px;height:186px}
</style>
</head>
<body>

<svg class="hidden-defs" aria-hidden="true">
  <symbol id="i-phone" viewBox="0 0 24 24"><path d="M6.6 2.5c.6-.4 1.4-.3 1.8.3l2.2 3.4c.4.6.3 1.4-.3 1.8L8.7 9c.9 2.6 3.6 5.5 6.3 6.6l1.1-1.6c.4-.6 1.2-.7 1.8-.3l3.4 2.2c.6.4.7 1.2.3 1.8l-1.4 2.2c-.8 1.2-2.3 1.7-3.6 1.2C10 19 5 14 2.8 7.4c-.4-1.3.1-2.8 1.3-3.6z"/></symbol>
  <symbol id="i-mail" viewBox="0 0 24 24"><path d="M2 5h20v14H2zm2 2.2V17h16V7.2l-8 5.4zM5.3 7l6.7 4.5L18.7 7z"/></symbol>
  <symbol id="i-cursor" viewBox="0 0 24 24"><path d="M3 3l17 7-6.6 2.2 5.8 5.8-2.2 2.2-5.8-5.8L9 21z"/></symbol>
  <symbol id="i-globe" viewBox="0 0 24 24"><path d="M12 2a10 10 0 1 0 0 20 10 10 0 0 0 0-20zm0 2c1.3 1.5 2.2 3.6 2.4 7H9.6c.2-3.4 1.1-5.5 2.4-7zM8.6 4.7C8 6.3 7.6 8.5 7.6 11H4.1a8 8 0 0 1 4.5-6.3zm6.8 0A8 8 0 0 1 19.9 11h-3.5c0-2.5-.4-4.7-1-6.3zM4.1 13h3.5c.1 2.5.4 4.7 1 6.3A8 8 0 0 1 4.1 13zm5.5 0h4.8c-.2 3.4-1.1 5.5-2.4 7-1.3-1.5-2.2-3.6-2.4-7zm6.8 0h3.5a8 8 0 0 1-4.5 6.3c.6-1.6.9-3.8 1-6.3z"/></symbol>
</svg>

<!-- Sticker 1 -->
<div class="sticker s1">
  <div class="s1__inner">
    <div class="s1__top"></div>
    <svg class="s1__swoosh" width="480" height="41" viewBox="0 0 480 41" aria-hidden="true">
      <path d="M350 41 C385 8 410 0 440 0 L480 0 L480 41 Z" fill="var(--navy)"/>
      <path d="M418 0 C428 24 452 40 480 41 L480 34 C458 32 443 18 440 0 Z" fill="var(--orange)"/>
      <path d="M440 0 C443 18 458 32 480 34 L480 0 Z" fill="var(--green)"/>
    </svg>
    <div class="line" style="left:14px;top:14px;font-size:13.5px">
      <svg class="icon" width="14" height="14" style="margin-right:8px"><use href="#i-cursor"/></svg>www.velnorix.srl
      <svg class="icon" width="15" height="15" style="margin:0 6px 0 14px"><use href="#i-mail"/></svg>office@velnorix.srl
    </div>
    <div class="brand-square" style="left:7px;top:54px;width:56px;height:55px;background:var(--white)"></div>
    <div class="wordmark wordmark--white" style="left:86px;top:56px;font-size:58px">VELNORIX</div>
    <div class="s1__bottom">
      <div class="line" style="left:84px;top:4px;font-size:35px;font-weight:600">
        <svg class="icon" width="20" height="20" style="margin-right:6px"><use href="#i-phone"/></svg>+39 312 5550148
      </div>
    </div>
  </div>
</div>

<!-- Sticker 2 -->
<div class="sticker s2">
  <div class="brand-square" style="left:12px;top:10px;width:107px;height:107px;background:var(--navy)"></div>
  <div class="wordmark wordmark--navy" style="left:132px;top:6px;font-size:60px">VELNORIX</div>
  <div class="tagline"><span class="c-navy">CLEANING</span><span class="c-navy">•</span><span class="c-green">GARDENING</span><span class="c-orange">•PESTCONTROL</span></div>
  <div class="contact-bar" style="left:132px;width:121px;background:var(--navy)">
    <span class="badge" style="border-color:var(--navy);color:var(--navy)"><svg class="icon" width="12" height="12"><use href="#i-phone"/></svg></span>
    <span class="line" style="left:16px;top:9px">+39 312 5550148</span>
  </div>
  <div class="contact-bar" style="left:257px;width:137px;background:var(--green)">
    <span class="badge" style="border-color:var(--green);color:var(--green)"><svg class="icon" width="13" height="13"><use href="#i-globe"/></svg></span>
    <span class="line" style="left:26px;top:9px">www.velnorix.srl</span>
  </div>
  <div class="contact-bar" style="left:398px;width:141px;background:var(--orange)">
    <span class="badge" style="border-color:var(--orange);color:var(--orange)"><svg class="icon" width="13" height="13"><use href="#i-mail"/></svg></span>
    <span class="line" style="left:18px;top:9px">office@velnorix.srl</span>
  </div>
</div>

<!-- Sticker 3 -->
<div class="sticker s3">
  <div class="wordmark wordmark--navy" style="left:19px;top:14px;font-size:58px">VELNORIX</div>
  <div class="brand-square" style="left:19px;top:75px;width:110px;height:110px;background:var(--navy)"></div>
  <div class="abs" style="left:137px;top:75px;width:270px;height:45px;background:var(--navy)">
    <div class="line" style="left:10px;top:9px;font-size:27px;font-weight:600">
      <svg class="icon" width="18" height="18" style="margin-right:8px;color:var(--orange)"><use href="#i-phone"/></svg>+39 312 5550148
    </div>
  </div>
  <div class="abs" style="left:137px;top:120px;width:270px;height:65px;background:var(--green)">
    <div class="line" style="left:12px;top:10px;font-size:19.5px;font-weight:500">
      <svg class="icon" width="14" height="14" style="margin-right:9px"><use href="#i-mail"/></svg>office@velnorix.srl
    </div>
    <div class="line" style="left:12px;top:34px;font-size:19.5px;font-weight:500">
      <svg class="icon" width="13" height="13" style="margin-right:10px"><use href="#i-cursor"/></svg>www.velnorix.srl
    </div>
  </div>
</div>

<!-- Sticker 4 -->
<div class="sticker s4">
  <div class="abs" style="left:13px;top:13px;width:480px;height:70px;background:var(--navy)">
    <div class="brand-square" style="left:7px;top:6px;width:56px;height:56px;background:var(--white)"></div>
    <div class="wordmark wordmark--white" style="left:86px;top:7px;font-size:58px">VELNORIX</div>
  </div>
  <div class="abs" style="left:13px;top:83px;width:480px;height:55px;background:var(--orange)">
    <div class="line" style="left:49px;top:8px;font-size:38px;font-weight:600">
      <svg class="icon" width="22" height="22" style="margin-right:14px"><use href="#i-phone"/></svg>+39 312 5550148
    </div>
  </div>
  <div class="abs" style="left:13px;top:138px;width:240px;height:34px;background:var(--green)">
    <div class="line" style="left:24px;top:9px;font-size:15.5px;font-weight:500">
      <svg class="icon" width="19" height="19" style="margin-right:7px"><use href="#i-mail"/></svg>office@velnorix.srl
    </div>
  </div>
  <div class="abs" style="left:253px;top:138px;width:240px;height:34px;background:var(--navy)">
    <div class="line" style="left:24px;top:9px;font-size:15.5px;font-weight:500">
      <svg class="icon" width="16" height="16" style="margin-right:20px"><use href="#i-cursor"/></svg>www.velnorix.srl
    </div>
  </div>
</div>

</body>
</html>
```